Social Media Cover and Profile

We already have our own logo. We just need a fresh design on our social media pages. We are not happy with our current designs. We would like to incorporate our YIKE billboard and the colors are blue (#05143f) and white. You can also incorporate silver as well. We are a family law office (Divorce and Custody) We no longer want to incorporate the Spire of Dunvale photo that we are currently using. You can look at our Facebook page; The Law Office of Miles T. Hadley.

Target Market(s)

Potential Clients

Industry/Entity Type

Family Law

Logo Text

Our Logo Is The Law Office of Miles T. Hadley with the Sheild

Requirements
Must have
• Text to include:
Central Pennslyvania's Premier Family Law Firm

Ability to be resized to and used as all images in social media, including but not limited to: Youtube Channel art, Facebook Cover and Profile.
Nice to have
• Darker color but we are open to "bright" ideas.

```html
<!DOCTYPE html>
<html lang="en">
<head>
<meta charset="utf-8">
<title>The Law Office of Miles T. Hadley – Cover</title>
<link href="https://fonts.googleapis.com/css2?family=EB+Garamond:wght@400;600;700&family=Montserrat:wght@600;800&display=swap" rel="stylesheet">
<style>
  :root {
    --navy: #05143f;
    --white: #ffffff;
    --silver: #8f9297;
    --silver-light: #e4e5e8;
    --ink: #1b1b1f;
    --stage: #e9e9ec;
  }
  html, body {
    margin: 0;
    padding: 0;
    width: 1200px;
    height: 1200px;
    overflow: hidden;
    background: var(--stage);
  }
  .cover {
    position: absolute;
    left: 30px;
    top: 383px;
    width: 1140px;
    height: 434px;
    display: flex;
    box-shadow: 0 18px 30px rgba(0,0,0,0.18);
  }
  .cover-statement {
    width: 448px;
    height: 100%;
    background: var(--navy);
    color: var(--white);
    box-sizing: border-box;
    padding: 78px 0 0 58px;
    font-family: "EB Garamond", Georgia, serif;
    font-size: 52px;
    line-height: 64px;
  }
  .cover-statement span { display: block; white-space: nowrap; }
  .cover-statement .strong { font-weight: 700; }
  .cover-statement .light { font-weight: 400; }
  .cover-billboard {
    position: relative;
    flex: 1;
    background: var(--white);
  }
  .firm-name {
    position: absolute;
    top: 44px;
    right: 46px;
    display: flex;
    align-items: center;
    gap: 12px;
    color: var(--navy);
    font-family: "EB Garamond", Georgia, serif;
    font-weight: 600;
  }
  .firm-name .mark {
    width: 44px;
    height: 44px;
    background: var(--navy);
  }
  .firm-name .lines { line-height: 1; }
  .firm-name .small { display: block; font-size: 11px; letter-spacing: 0.5px; }
  .firm-name .large { display: block; font-size: 24px; letter-spacing: 0.5px; }
  .rings {
    position: absolute;
    left: 40px;
    top: 118px;
    width: 200px;
    height: 190px;
    border-radius: 12px;
    background: radial-gradient(ellipse at center, var(--white) 30%, var(--silver-light) 100%);
  }
  .billboard-word {
    position: absolute;
    left: 248px;
    top: 118px;
    font-family: "Montserrat", Arial, sans-serif;
    font-weight: 800;
    font-size: 170px;
    line-height: 190px;
    letter-spacing: -6px;
    color: var(--silver);
  }
  .practice-line {
    position: absolute;
    left: 0;
    right: 0;
    top: 344px;
    text-align: center;
    font-family: "Montserrat", Arial, sans-serif;
    font-weight: 600;
    font-size: 20px;
    letter-spacing: 3px;
    color: var(--ink);
  }
  .practice-line .focus { color: var(--navy); }
</style>
</head>
<body>
  <section class="cover">
    <div class="cover-statement">
      <span class="light">Central</span>
      <span class="strong">Pennsylvania's</span>
      <span class="strong">Premier Family</span>
      <span class="light">Law Firm</span>
    </div>
    <div class="cover-billboard">
      <div class="firm-name">
        <div class="mark"></div>
        <div class="lines">
          <span class="small">THE LAW OFFICE OF</span>
          <span class="large">MILES T HADLEY</span>
        </div>
      </div>
      <div class="rings" role="img" aria-label="Photo of a silver wedding band and a diamond engagement ring standing upright"></div>
      <div class="billboard-word">YIKE</div>
      <div class="practice-line">FAMILY LAWYER <span class="focus">(DIVORCE AND CUSTODY)</span></div>
    </div>
  </section>
</body>
</html>
```